Velvet Harbor for sale at the 2019 Tandor Crest Mare Auction on 30 May 2019

I am selling my broodmare at the 2019 Tandor Crest Mare auction on 30 May 2019. I need a flyer to hand out to potential buyers. I have included the required information in the attached word document. I can provide more images if required. I am thinking that a DL double sided or an A5 will suit best. I'm happy to provide more information as required.

Target Market(s)

Race horse breeders, people who buy broodmares.

Font styles to use
Serif
Sans Serif
Script

Colors

Designer to choose colors to be used in the design.

Requirements
Must have
• All of the content provided in the attached brief, however it is not necessary to have the words exactly as per the brief. The brief is for information purposes.
Nice to have
• Innovation...

```html
<!DOCTYPE html>
<html lang="en">
<head>
<meta charset="utf-8">
<title>Velvet Harbor – Tandor Crest Mare Auction</title>
<link rel="stylesheet" href="https://fonts.googleapis.com/css2?family=Roboto+Condensed:ital,wght@0,400;0,700;1,400;1,700&family=Lobster&display=swap">
<style>
  :root {
    --red: #d42027;
    --yellow: #f8bd2b;
    --black: #050505;
    --grey: #3d3d3d;
    --white: #ffffff;
    --ink: #1a1a1a;
    --page: #f2f2f2;
    --turf: #5f9e3a;
    --turf-light: #8cc55a;
    --sky: #b9d3e6;
  }
  * { margin: 0; padding: 0; box-sizing: border-box; }
  html, body { width: 1200px; height: 1200px; overflow: hidden; background: var(--page); }
  body { position: relative; font-family: "Roboto Condensed", "Arial Narrow", sans-serif; }

  .flyer {
    position: absolute; left: 214px; top: 48px;
    width: 772px; height: 1104px;
    background: var(--black); overflow: hidden;
  }
  .flyer-bg { position: absolute; inset: 0; }

  .title-band {
    position: absolute; left: 0; top: 34px; width: 394px; height: 78px;
    background: linear-gradient(90deg, var(--red) 0%, var(--red) 70%, rgba(212,32,39,0) 100%);
  }
  .title {
    position: absolute; left: 43px; top: 38px;
    font-size: 62px; font-weight: 700; font-style: italic; color: var(--white);
    letter-spacing: -1px; line-height: 70px; white-space: nowrap;
  }

  .record-tab {
    position: absolute; left: 574px; top: 34px; width: 198px; height: 26px;
    background: var(--yellow); clip-path: polygon(5% 0, 100% 0, 100% 100%, 0 100%);
  }
  .record-heading {
    position: absolute; right: 42px; top: 34px;
    font-size: 23px; font-weight: 700; font-style: italic; color: var(--ink); line-height: 27px;
  }
  .record-line {
    position: absolute; right: 42px;
    font-size: 20px; font-style: italic; color: var(--white); line-height: 24px; white-space: nowrap;
  }
  .record-line b { font-weight: 700; font-size: 23px; }
  .record-mark {
    position: absolute; right: 0; width: 22px; height: 18px; background: var(--red);
    clip-path: polygon(20% 0, 100% 0, 100% 100%, 0 100%);
  }

  .race-photo {
    position: absolute; border-radius: 50%; border: 6px solid var(--white);
    background: linear-gradient(180deg, var(--sky) 0%, #6f8b6a 38%, var(--turf) 55%, var(--turf-light) 100%);
    box-shadow: 0 4px 14px rgba(0,0,0,0.45);
  }

  .caption {
    position: absolute; width: 320px; text-align: center; color: var(--white);
    text-transform: uppercase; line-height: 13.5px; font-size: 11px;
  }
  .caption strong { display: block; font-size: 13.5px; font-weight: 700; line-height: 16px; }

  .lot-bar { position: absolute; left: 0; top: 1018px; width: 11px; height: 48px; background: var(--yellow); }
  .lot-info {
    position: absolute; left: 42px; top: 1014px;
    font-size: 24px; font-style: italic; color: var(--white); line-height: 27px;
  }
  .sale-word {
    position: absolute; left: 290px; top: 982px;
    font-family: "Lobster", cursive; font-size: 92px; color: var(--yellow); line-height: 100px;
  }
  .sale-details {
    position: absolute; left: 463px; top: 990px;
    font-style: italic; font-weight: 700; text-transform: uppercase; line-height: 26px;
  }
  .sale-date { font-size: 27px; color: var(--white); line-height: 28px; }
  .sale-event { font-size: 23px; color: var(--yellow); }
</style>
</head>
<body>
<main class="flyer">
  <svg class="flyer-bg" width="772" height="1104" viewBox="0 0 772 1104" aria-hidden="true">
    <defs>
      <linearGradient id="greySweep" x1="0" y1="0" x2="1" y2="1">
        <stop offset="0" stop-color="#4a4a4a"/>
        <stop offset="1" stop-color="#2a2a2a"/>
      </linearGradient>
    </defs>
    <path d="M362 0 L772 0 L772 600 C700 400 560 120 362 0 Z" fill="url(#greySweep)"/>
    <path d="M0 1004 C300 960 620 800 772 552 L772 1104 L0 1104 Z" fill="var(--red)"/>
  </svg>

  <div class="title-band"></div>
  <h1 class="title">VELVET HARBOR</h1>

  <div class="record-tab"></div>
  <h2 class="record-heading">RACE RECORD</h2>
  <p class="record-line" style="top:64px"><b>7</b> WINS <b>2</b> SECONDS</p>
  <span class="record-mark" style="top:69px"></span>
  <p class="record-line" style="top:90px"><b>2</b> THIRDS (27-7:2:2)</p>
  <span class="record-mark" style="top:95px"></span>
  <p class="record-line" style="top:116px"><b>$ 205,400</b> PRIZE MONEY</p>
  <span class="record-mark" style="top:121px"></span>

  <p class="caption" style="left:3px; top:186px"><strong>Velvet Harbor wins by 2.8L</strong>No more than one metro win handicap - 1400m<br>Riverbend Racing Club (Kestrel Park)<br>10 December 2016</p>
  <p class="caption" style="left:448px; top:210px"><strong>Velvet Harbor beats Silver Lantern by 1.3L</strong>Class 6 plate - 1300m<br>Riverbend Racing Club (Kestrel Park)<br>29 April 2017</p>

  <div class="race-photo" role="img" aria-label="Photo: Velvet Harbor winning at Kestrel Park, December 2016" style="left:19px; top:244px; width:288px; height:288px"></div>
  <div class="race-photo" role="img" aria-label="Photo: Velvet Harbor winning at Linden Downs, November 2016" style="left:-6px; top:520px; width:280px; height:280px"></div>
  <div class="race-photo" role="img" aria-label="Photo: Velvet Harbor beating Silver Lantern at Kestrel Park, April 2017" style="left:454px; top:268px; width:312px; height:312px"></div>
  <div class="race-photo" role="img" aria-label="Photo: Velvet Harbor winning on debut at Coral Coast" style="left:474px; top:568px; width:288px; height:288px"></div>
  <div class="race-photo" role="img" aria-label="Photo: Velvet Harbor winning at Kestrel Park, January 2017" style="left:203px; top:400px; width:368px; height:368px"></div>

  <p class="caption" style="left:226px; top:786px"><strong>Velvet Harbor wins by 3.5L</strong>Class 6 handicap - 1400m<br>Riverbend Racing Club (Kestrel Park)<br>21 January 2017</p>
  <p class="caption" style="left:-37px; top:820px"><strong>Velvet Harbor wins by 2.3L</strong>Class 4 handicap - 1400m<br>Riverbend Racing Club (Linden Downs)<br>23 November 2016</p>
  <p class="caption" style="left:456px; top:868px"><strong>Velvet Harbor wins on debut</strong>Maiden - 1000m<br>Coral Coast Turf Club<br>23 October 2015</p>

  <div class="lot-bar"></div>
  <p class="lot-info">LOT NUMBER:1414<br>STABLE: QC 6</p>
  <p class="sale-word">Sale</p>
  <div class="sale-details">
    <p class="sale-date">30 May 2019</p>
    <p class="sale-event">2019 Tandor Crest Mare<br>Auction</p>
  </div>
</main>
</body>
</html>
```